political advertisement for magazine

9.135 in 12.125 in. My wife is running for Judge. She needs an ad for an African-American Magazine ASAP . The ad is about a testimonial by one of her clients that makes her relatable to the African-American community. I am uploading the text for the testimonial, the picture of my wife and her client, her logo, a possible backdrop and also a slogan.

Target Market(s)

This is going in a church publication geared toward the African American Community

Requirements
Nice to have
• The image of all the people in the back. On top of that image, you have "The people stand behind Delphine for Circuit Court Judge". Also you have a letter from her client with a picture of both of them. Also include the vote for Delphine logo and her headshot. The above is just my idea if you have an idea that is totally different but portrays that Delphine is for the people, I am ok with that too. thanks!

```html
<!DOCTYPE html>
<html lang="en">
<head>
<meta charset="utf-8">
<title>Delphine Okafor Bell for Circuit Court Judge – Magazine Ad</title>
<link rel="stylesheet" href="https://fonts.googleapis.com/css2?family=Cinzel:wght@700&family=Jost:wght@400;500;600&display=swap">
<style>
  :root {
    --stage: #e9eaec;
    --paper: #ffffff;
    --frame-red: #e0262f;
    --headline-red: #e0343c;
    --navy: #1f3a78;
    --ink: #2b2b2b;
    --ink-strong: #111111;
    --faces-light: #eeeeee;
    --faces-mid: #d6d6d6;
    --white: #ffffff;
  }
  * { box-sizing: border-box; margin: 0; padding: 0; }
  html, body {
    width: 1200px; height: 920px; overflow: hidden;
    background: var(--stage);
  }
  .ad-page {
    position: absolute; left: 270px; top: 22px;
    width: 660px; height: 876px;
    background: var(--paper);
    border: 9px solid var(--frame-red);
    overflow: hidden;
    box-shadow: 0 6px 24px rgba(0,0,0,.18);
    font-family: "Jost", sans-serif;
  }
  .crowd-backdrop {
    position: absolute; inset: 0 0 330px 0;
    background:
      radial-gradient(ellipse at 20% 30%, var(--faces-mid) 0%, transparent 45%),
      radial-gradient(ellipse at 75% 60%, var(--faces-mid) 0%, transparent 50%),
      linear-gradient(180deg, var(--faces-light), #f6f6f6);
    opacity: .8;
  }
  .ad-headline {
    position: absolute; left: 34px; top: 40px; width: 590px;
    font-family: "Cinzel", serif; font-weight: 700;
    font-size: 25px; line-height: 1.15;
    color: var(--headline-red); text-transform: uppercase;
  }
  .testimonial {
    position: absolute; left: 34px; top: 122px; width: 580px;
    color: var(--ink); font-size: 15px; line-height: 1.45;
  }
  .testimonial p { margin-bottom: 14px; }
  .testimonial .sign-off { margin-top: 22px; line-height: 1.3; }
  .testimonial .signer { font-weight: 600; color: var(--ink-strong); }
  .client-photo {
    position: absolute; left: 378px; top: 330px;
    width: 240px; height: 176px;
    border: 6px solid var(--white);
    box-shadow: 0 4px 12px rgba(0,0,0,.3);
    background: linear-gradient(160deg, #5f8a4f 0%, #b96a7a 35%, #c9d6e4 70%, #e9e9ee 100%);
    z-index: 2;
  }
  .vote-band {
    position: absolute; left: 0; right: 0; bottom: 0; height: 330px;
    background: var(--navy);
  }
  .candidate-headshot {
    position: absolute; left: 130px; bottom: 0;
    width: 280px; height: 420px;
    border-radius: 140px 140px 0 0;
    background: linear-gradient(180deg, #7a5a44 0%, #c99b80 35%, #1c1c20 62%, #15151a 100%);
    z-index: 3;
  }
  .campaign-name {
    position: absolute; left: 420px; top: 600px; width: 210px;
    text-align: center; color: var(--white);
    font-family: "Jost", sans-serif; font-weight: 500;
    text-transform: uppercase; font-size: 17px; line-height: 1.25;
    letter-spacing: 1px;
  }
  .campaign-name .name-line { font-size: 26px; }
  .disclaimer {
    position: absolute; left: 420px; top: 730px; width: 210px;
    text-align: center; color: var(--white);
    font-size: 11px; line-height: 1.35;
  }
</style>
</head>
<body>
  <article class="ad-page">
    <div class="crowd-backdrop" role="img" aria-label="Faded collage of many smiling community members' portraits"></div>

    <h1 class="ad-headline">The people stand behind Delphine<br>for Circuit Court Judge</h1>

    <section class="testimonial">
      <p>For the past few years, Delphine Okafor Bell has been my lawyer. She has always strived to provide excellence in legal services. Her almost encyclopedic knowledge of the law makes for a flawless, precise, navigation of the legal system, with results.</p>
      <p>She is the epitome of professionalism, that is aptly balanced by her calm persona. Her empathy is more than commendable, and her legal experience unmatched.</p>
      <p>Delphine Okafor Bell is truly one of kind, deserving of all accolades, appointments, and accomplishments.</p>
      <p class="sign-off">Yours Truly,<br><span class="signer">Lionel Pratt</span></p>
    </section>

    <div class="client-photo" role="img" aria-label="Photo of the candidate shaking hands with her client in front of a flowering garden"></div>

    <div class="vote-band"></div>
    <div class="candidate-headshot" role="img" aria-label="Portrait of the candidate in a dark blazer and pearl necklace"></div>

    <div class="campaign-name">
      Vote<br><span class="name-line">Delphine</span><br>Okafor Bell<br>for Judge
    </div>
    <p class="disclaimer">Political Advertisement paid for and approved by the Committee to Elect Delphine Okafor Bell, no party affiliation, for Circuit Court Judge</p>
  </article>
</body>
</html>
```